Block makes the buck for writing

We need a notepad in DIN A4 format which we can give to our customers at events. We, TROVALK, are active in the field of safe electrical engineering and offer software, hardware, academia and consulting in this field. With our software can be z. For example, you can quickly and easily inventory and document all equipment and equipment. Every tool must be checked in Germany and the test repeated at regular intervals. The appropriate test specifications are stored in our software. In addition to the software, we also offer measuring and testing equipment. In our academy, we also offer seminars on various areas of safe electrical engineering. Our consulting advises companies on the establishment of a legally compliant company organization. If necessary, our experts also take on the temporary function of external responsible electrician. So we offer an all-round package concerning safe electrical engineering. TROVALK makes working with electricity safe. Every year we offer an event with different workshops. There the users of our software are invited. You can exchange ideas with our lecturers and experts and exchange experiences and tips with each other. For this event we need a writing pad where participants can take their notes throughout the day. In addition, the block should also be used by customers. But it would be nice if he had a special feature / a special feature by which he is particularly happy to use. As basic the block should be branded with our logo and our URL (trovalk.de).

```html
<!DOCTYPE html>
<html lang="de">
<head>
<meta charset="utf-8">
<title>TROVALK Notizblock</title>
<link rel="stylesheet" href="https://fonts.googleapis.com/css2?family=Open+Sans:wght@400;700&display=swap">
<style>
  :root {
    --backdrop: #c9c9c9;
    --cover-paper: #f8f8f8;
    --sheet-paper: #ffffff;
    --ink: #4a4a46;
    --accent: #f5a01a;
    --rule: #e2e2e2;
    --memo-field: #f7f7f7;
    --memo-tab: #c4c4c4;
  }
  * { margin: 0; padding: 0; box-sizing: border-box; }
  html, body {
    width: 1200px; height: 877px; overflow: hidden;
    background: var(--backdrop);
    font-family: "Open Sans", sans-serif;
    color: var(--ink);
  }
  .canvas { position: relative; width: 1200px; height: 877px; }
  .page {
    position: absolute; top: 104px; width: 484px; height: 680px;
  }
  .page--cover { left: 83px; background: var(--cover-paper); }
  .page--sheet { left: 634px; background: var(--sheet-paper); }

  .brand {
    position: absolute; display: flex; align-items: center;
    font-weight: 700; color: var(--ink); letter-spacing: -0.5px;
  }
  .brand__dot { border-radius: 50%; background: var(--accent); margin-left: 14px; }
  .page--cover .brand { right: 62px; top: 580px; font-size: 31px; }
  .page--cover .brand__dot { width: 43px; height: 43px; }
  .page--sheet .brand { right: 38px; top: 58px; font-size: 26px; }
  .page--sheet .brand__dot { width: 36px; height: 36px; margin-left: 12px; }

  .site {
    position: absolute; left: 60px; top: 72px;
    display: flex; align-items: center; font-size: 12px;
  }
  .site__marker { width: 7px; height: 7px; background: var(--accent); margin-right: 9px; }
  .site__name { font-weight: 700; }

  .ruled { position: absolute; left: 38px; width: 408px; }
  .ruled--notes { top: 141px; }
  .ruled__line { height: 23.2px; border-bottom: 1px solid var(--rule); }

  .memo {
    position: absolute; left: 38px; top: 417px; width: 408px; height: 231px;
    background: var(--memo-field);
  }
  .memo__tab {
    position: absolute; left: 22px; top: 1px; height: 20px; padding: 0 7px;
    background: var(--memo-tab); color: #fff; font-size: 10.5px; line-height: 20px;
    border-radius: 2px;
  }
  .memo .ruled { left: 22px; width: 362px; top: 29px; }
  .memo .ruled__line { height: 22.95px; }
</style>
</head>
<body>
<main class="canvas">
  <section class="page page--cover" aria-label="Deckblatt">
    <div class="brand"><span class="brand__name">TROVALK</span><span class="brand__dot"></span></div>
  </section>

  <section class="page page--sheet" aria-label="Notizseite">
    <div class="site"><span class="site__marker"></span><span class="site__name">trovalk</span>.de</div>
    <div class="brand"><span class="brand__name">TROVALK</span><span class="brand__dot"></span></div>

    <div class="ruled ruled--notes">
      <div class="ruled__line"></div><div class="ruled__line"></div><div class="ruled__line"></div>
      <div class="ruled__line"></div><div class="ruled__line"></div><div class="ruled__line"></div>
      <div class="ruled__line"></div><div class="ruled__line"></div><div class="ruled__line"></div>
      <div class="ruled__line"></div><div class="ruled__line"></div><div class="ruled__line"></div>
    </div>

    <div class="memo">
      <span class="memo__tab">Das merk ich mir!</span>
      <div class="ruled">
        <div class="ruled__line"></div><div class="ruled__line"></div><div class="ruled__line"></div>
        <div class="ruled__line"></div><div class="ruled__line"></div><div class="ruled__line"></div>
        <div class="ruled__line"></div><div class="ruled__line"></div>
      </div>
    </div>
  </section>
</main>
</body>
</html>
```